Billboard advertisement design

Health & Fitness centre requires a billboard advertisement design for an allocated space out the front of the shopping centre in which it is located. Bolt Ridge Health & Fitness is located in a small town with one other competitor. Looking for a fun, trendy sign to draw people's attention and make sure Bolt Ridge is instantly recognisable. Sign location is in the middle of town on the national highway. Approximate size is 12' x 5'. Final design will encourage people who have been thinking about joining the gym to take the first step in leading a fitter and healthier lifestyle.

Target Market(s)

Health conscious members of the community that have been thinking about taking the next step and joining a gym

Industry/Entity Type

Shopping

Requirements
Must have
• Please utilise attached logo
Nice to have
• Contact info is (07) 4913 5862 info@boltridgefitness-example.com.au

```html
<!DOCTYPE html>
<html lang="en">
<head>
<meta charset="utf-8">
<title>Bolt Ridge Health &amp; Fitness – Billboard</title>
<link rel="stylesheet" href="https://fonts.googleapis.com/css2?family=Russo+One&family=Open+Sans:wght@700&display=swap">
<style>
  :root {
    --page-bg: #ffffff;
    --sky-top: #1f6fc4;
    --sky-mid: #5fb0ea;
    --sky-pale: #cfeaf9;
    --ridge-dark: #2f2f31;
    --ridge-mid: #454548;
    --brand-navy: #17437e;
    --phone-blue: #2a8ad8;
    --phone-orange: #f07a1a;
    --text-white: #ffffff;
  }
  * { margin: 0; padding: 0; box-sizing: border-box; }
  html, body {
    width: 1200px;
    height: 600px;
    overflow: hidden;
    background: var(--page-bg);
  }
  .canvas {
    position: relative;
    width: 1200px;
    height: 600px;
    display: flex;
    align-items: center;
    justify-content: center;
  }
  .billboard {
    position: relative;
    width: 1200px;
    height: 500px;
    overflow: hidden;
    background: radial-gradient(ellipse at 45% 30%, var(--sky-pale) 0%, var(--sky-mid) 45%, var(--sky-top) 100%);
  }
  .billboard__scene {
    position: absolute;
    left: 0;
    top: 0;
    width: 1200px;
    height: 500px;
  }
  .brand {
    position: absolute;
    top: 30px;
    left: 0;
    width: 100%;
    text-align: center;
    color: var(--brand-navy);
    font-family: "Russo One", sans-serif;
    font-weight: 400;
  }
  .brand__name {
    display: block;
    font-size: 118px;
    line-height: 1;
    letter-spacing: 2px;
  }
  .brand__tag {
    display: block;
    margin-top: 18px;
    font-size: 34px;
    line-height: 1;
    letter-spacing: 92px;
    padding-left: 92px;
  }
  .contact {
    position: absolute;
    left: 0;
    width: 100%;
    text-align: center;
  }
  .contact__phone {
    top: 348px;
    font-family: "Russo One", sans-serif;
    font-size: 88px;
    line-height: 1;
    letter-spacing: 3px;
  }
  .contact__area { color: var(--phone-blue); }
  .contact__number { color: var(--phone-orange); }
  .contact__email {
    top: 446px;
    font-family: "Open Sans", sans-serif;
    font-weight: 700;
    font-size: 40px;
    line-height: 1;
    color: var(--text-white);
  }
</style>
</head>
<body>
  <main class="canvas">
    <section class="billboard">
      <svg class="billboard__scene" viewBox="0 0 1200 500" role="img" aria-label="Dark rocky ridge silhouette with people stretching, running and climbing along the skyline">
        <defs>
          <linearGradient id="ridgeFill" x1="0" y1="0" x2="0" y2="1">
            <stop offset="0" stop-color="var(--ridge-mid)" stop-opacity="0"/>
            <stop offset="0.18" stop-color="var(--ridge-mid)" stop-opacity="0.85"/>
            <stop offset="0.45" stop-color="var(--ridge-dark)"/>
            <stop offset="1" stop-color="var(--ridge-dark)"/>
          </linearGradient>
        </defs>
        <rect x="0" y="230" width="1200" height="270" fill="url(#ridgeFill)"/>
      </svg>

      <h1 class="brand">
        <span class="brand__name">BOLT RIDGE</span>
        <span class="brand__tag">FITNESS</span>
      </h1>

      <p class="contact contact__phone">
        <span class="contact__area">(07)</span>
        <span class="contact__number">4913 5862</span>
      </p>
      <p class="contact contact__email">info@boltridgefitness-example.com.au</p>
    </section>
  </main>
</body>
</html>
```